Harborline Power Works, LLC New Business Card Design Project

Please do not submit multiple designs that look similar. Many submittals of nearly the same design will result in auto rejection. Please do not submit a design unless you know how to provide a PDF with recognizable text that I can modify and update using Adobe Acrobat. I do not use Adobe Photoshop. Please design a business card using the attached HPW logo. Be creative. Do at least 2-3 different designs. One side should have the logo large with the URL www.HPW-KV.com. The other side of the card should have the name Marcus Pellow. License number 524038. Phone number 860-555-0143. Email service@HPW-KV.com. Physical address 742 Maple Orchard Road, Suite 8, Brookfield Falls, VT. 06099. The company name should also be spelled out somewhere, Harborline Power Works, LLC. Please ensure there is no tiny font. Please also ensure that there is nothing near the edges that might get cut off during printing. It will be 3.5" x 2" horizontal standard business card. I use CardQuarry.com to order. The customer has said they want the business card to use the attached look and color scheme. Please do not submit a design unless you know how to provide a PDF with recognizable text that I can modify and update using Adobe Acrobat. I do not use Adobe Photoshop.
Target Market(s)
Read all instructions above.
Industry/Entity Type
Contact Information for Business Card
Requirements
Must have
- Read all instructions above.
Nice to have
Should not have

```html
<!DOCTYPE html>
<html lang="en">
<head>
<meta charset="utf-8">
<title>Harborline Power Works, LLC — Business Card</title>
<link href="https://fonts.googleapis.com/css2?family=Poppins:wght@400;500;700&display=swap" rel="stylesheet">
<style>
  :root {
    --backdrop: #dcdddf;
    --card-white: #ffffff;
    --card-black: #050505;
    --ink: #1a1a1a;
    --ink-strong: #000000;
    --rule: #6f6f6f;
    --silver: #7a7a7a;
    --gold: #c9a43a;
    --paper-text: #f2f2f2;
  }
  * { box-sizing: border-box; margin: 0; padding: 0; }
  html, body {
    width: 1200px; height: 1200px; overflow: hidden;
    background: var(--backdrop);
    font-family: "Poppins", sans-serif;
  }
  .card {
    position: absolute; left: 296px; width: 608px; height: 347px; overflow: hidden;
  }
  .card--front { top: 206px; background: var(--card-white); color: var(--ink); }
  .card--back { top: 646px; background: var(--card-black); color: var(--paper-text); }

  .brand {
    position: absolute; display: flex; flex-direction: column; align-items: center;
  }
  .brand__row { display: flex; align-items: center; gap: 10px; }
  .brand__dot { border-radius: 50%; }
  .brand__name { font-weight: 700; line-height: 1; letter-spacing: 1px; }
  .brand__license { font-weight: 500; letter-spacing: 1px; margin-top: 8px; }

  .card--front .brand { left: 22px; top: 52px; width: 144px; }
  .card--front .brand__dot { width: 16px; height: 16px; background: var(--silver); }
  .card--front .brand__name { font-size: 46px; color: var(--silver); }
  .card--front .brand__license { font-size: 11px; color: var(--silver); }

  .address {
    position: absolute; left: 22px; top: 209px;
    font-size: 14.5px; line-height: 20px;
  }
  .address-rule {
    position: absolute; left: 234px; top: 221px; width: 346px; height: 1px;
    background: var(--rule);
  }
  .contacts {
    position: absolute; left: 22px; top: 263px; list-style: none;
    font-size: 14.5px; line-height: 21px;
  }
  .contacts li { display: flex; align-items: center; gap: 8px; }
  .contacts svg { width: 12px; height: 12px; flex: none; }
  .holder-name {
    position: absolute; right: 28px; top: 293px;
    font-size: 26px; font-weight: 700; color: var(--ink-strong); letter-spacing: 0.5px;
  }
  .edge-tab {
    position: absolute; right: -10px; top: 299px; width: 20px; height: 23px;
    border-radius: 50%; background: var(--silver);
  }

  .pattern-field {
    position: absolute; inset: 0;
    background: linear-gradient(180deg, #0c0c0c 0%, #050505 50%, #0c0c0c 100%);
  }
  .card--back .brand { left: 96px; top: 135px; width: 170px; }
  .card--back .brand__dot { width: 18px; height: 18px; background: var(--gold); }
  .card--back .brand__name { font-size: 54px; color: var(--gold); }
  .card--back .brand__license { font-size: 12px; color: var(--gold); }
  .company-name {
    position: absolute; left: 26px; top: 308px;
    font-size: 14.5px; letter-spacing: 2px; text-transform: uppercase;
  }
</style>
</head>
<body>

<section class="card card--front">
  <div class="brand">
    <div class="brand__row">
      <span class="brand__dot"></span>
      <span class="brand__name">HPW</span>
    </div>
    <span class="brand__license">LIC-524038</span>
  </div>

  <p class="address">742 Maple Orchard Road<br>Suite 8, Brookfield Falls, VT. 06099</p>
  <div class="address-rule"></div>

  <ul class="contacts">
    <li>
      <svg viewBox="0 0 24 24" fill="none" stroke="currentColor" stroke-width="2"><path d="M5 3h4l2 5-3 2a12 12 0 0 0 6 6l2-3 5 2v4a2 2 0 0 1-2 2A17 17 0 0 1 3 5a2 2 0 0 1 2-2z"/></svg>
      860-555-0143
    </li>
    <li>
      <svg viewBox="0 0 24 24" fill="none" stroke="currentColor" stroke-width="2"><rect x="2" y="5" width="20" height="14"/><path d="M2 5l10 8 10-8"/></svg>
      service@HPW-KV.com
    </li>
    <li>
      <svg viewBox="0 0 24 24" fill="none" stroke="currentColor" stroke-width="2"><circle cx="12" cy="12" r="10"/><path d="M2 12h20M12 2a15 15 0 0 1 0 20M12 2a15 15 0 0 0 0 20"/></svg>
      www.HPW-KV.com
    </li>
  </ul>

  <h1 class="holder-name">MARCUS PELLOW</h1>
  <span class="edge-tab"></span>
</section>

<section class="card card--back">
  <div class="pattern-field" role="img" aria-label="Faint repeated company initials pattern across the black background"></div>
  <div class="brand">
    <div class="brand__row">
      <span class="brand__dot"></span>
      <span class="brand__name">HPW</span>
    </div>
    <span class="brand__license">LIC-524038</span>
  </div>
  <p class="company-name">Harborline Power Works, LLC</p>
</section>

</body>
</html>
```